Calm Fern Healthcare- Aged Care and Community Services

Looking for brochure to advertise our services. I will attach a draft that we do not want to use. Looking for graphics that are as natural as possible to present a personalised service. We supply services to aged people and people with disability. Please make it look classy and professional at the same time. I am looking for creativity. I have also attached the logo. Site addresses can be the last page. ideally looking for 2 designs, one A4 and another smaller possibly DL. Looking for creative out of the box thinkers. Thank you.

Target Market(s)

Aged Care service providers, disability service providers and private hospitals

Font styles to use
Serif
Sans Serif
Script

Colors
6b449b
886aae
eea4c8
f59195
fac994
3176b5
0555a3
cedeed
e4daeb

Requirements
Must have
• Targeted imagery, content and contact details
Nice to have
• personal profiles of people happy with our services

```html
<!DOCTYPE html>
<html lang="en">
<head>
<meta charset="utf-8">
<title>Calm Fern Healthcare – Brochure</title>
<link href="https://fonts.googleapis.com/css2?family=Barlow:wght@400;500;600;700&display=swap" rel="stylesheet">
<style>
  :root{
    --purple:#6b3a9b;
    --purple-light:#8a4fae;
    --purple-deep:#5e2f8f;
    --pink:#e6207a;
    --white:#ffffff;
    --ink:#333338;
    --backdrop:#3a3a3c;
    --paper:#fbfbfd;
  }
  *{margin:0;padding:0;box-sizing:border-box}
  html,body{width:875px;height:1200px;overflow:hidden}
  body{background:var(--backdrop);font-family:'Barlow',sans-serif;position:relative}
  .spread{position:absolute;left:86px;width:704px;height:497px;background:var(--paper);overflow:hidden}
  .spread--outer{top:86px}
  .spread--inner{top:615px}
  .abs{position:absolute}
  .photo{position:absolute}

  /* outer spread */
  .photo--card-game{left:0;top:0;width:352px;height:252px;background:linear-gradient(160deg,#6e5a92,#b8a6d4 55%,#564274)}
  .photo--high-five{left:352px;top:0;width:352px;height:306px;background:linear-gradient(135deg,#7fae4c,#d9d2bd 45%,#7fa9d0)}
  .cover-shape{position:absolute;left:0;top:0}
  .brand-name{position:absolute;font-weight:600;display:flex;align-items:center;gap:7px}
  .brand-name .dot{width:12px;height:12px;border-radius:50%;background:currentColor;flex:none}
  .brand-name--back{left:44px;top:318px;color:var(--white);font-size:20px}
  .brand-name--front{left:590px;top:344px;width:108px;color:var(--purple);font-size:14px;line-height:1.15}
  .contact{position:absolute;left:44px;top:364px;color:var(--white);font-weight:600;font-size:12px;list-style:none}
  .contact li{display:flex;align-items:center;gap:8px;height:18.5px}
  .contact svg{width:14px;height:14px;flex:none}
  .headline{position:absolute;left:380px;top:340px;color:var(--white);line-height:1}
  .headline span{display:block;font-size:25px;font-weight:500}
  .headline strong{display:block;font-size:30px;font-weight:700;margin-top:4px}
  .footer-band{position:absolute;left:0;bottom:0}
  .footer-url{position:absolute;bottom:10px;width:352px;text-align:center;color:var(--white);font-size:11px;letter-spacing:.2px}
  .footer-url--left{left:0}.footer-url--right{left:352px}

  /* inner spread */
  .services-box{position:absolute;left:0;top:29px;width:245px;height:131px;background:linear-gradient(90deg,var(--purple),var(--purple-light));padding:11px 12px 0 29px;color:var(--white)}
  .section-title{font-size:14px;font-weight:700;letter-spacing:.2px;display:inline-block;padding-bottom:3px;border-bottom:1.5px solid currentColor;padding-right:16px}
  .services-box p{font-size:7.6px;line-height:10.6px;margin-top:6px;font-weight:500}
  .personnel{position:absolute;left:29px;top:173px;width:210px;color:var(--ink)}
  .personnel p{font-size:10.5px;line-height:14.5px}
  .personnel ul{margin-top:8px;padding-left:14px;font-size:10.5px;line-height:14.6px}
  .photo--carer-walk{left:245px;top:29px;width:214px;height:383px;background:linear-gradient(120deg,#efe3cf,#d9c0a2 45%,#8b7565);clip-path:polygon(0 0,100% 0,100% 57.2%,50% 57.2%,50% 100%,0 100%)}
  .about{position:absolute;left:481px;top:40px;width:190px;color:var(--ink)}
  .about .section-title{color:var(--purple)}
  .about p{font-size:8.6px;line-height:11.4px;margin-top:8px}
  .criteria-frame{position:absolute;left:352px;top:250px;width:334px;height:202px;background:var(--white)}
  .criteria{position:absolute;left:359px;top:257px;width:320px;height:188px;background:linear-gradient(90deg,var(--purple-light),var(--purple))}
  .photo--team{left:7px;top:7px;width:146px;height:174px;background:linear-gradient(160deg,#f4f4f6,#c9b7a6 50%,#8fa6c4)}
  .criteria h3{position:absolute;left:162px;top:13px;width:152px;color:var(--white);font-size:7.6px;line-height:10px;font-weight:500}
  .criteria ul{position:absolute;left:173px;top:42px;width:142px;color:var(--white);font-size:6.1px;line-height:8.5px;font-weight:500;padding-left:0}
</style>
</head>
<body>

<section class="spread spread--outer">
  <div class="photo photo--card-game" role="img" aria-label="Purple-toned photo of a carer with elderly residents playing cards at an outdoor table"></div>
  <div class="photo photo--high-five" role="img" aria-label="Photo of a smiling nurse high-fiving an elderly woman outdoors"></div>

  <svg class="cover-shape" width="704" height="497" viewBox="0 0 704 497">
    <defs>
      <linearGradient id="coverPurple" x1="0" y1="0" x2="1" y2="1">
        <stop offset="0" stop-color="#6b3a9b"/><stop offset="1" stop-color="#8a4fae"/>
      </linearGradient>
    </defs>
    <rect x="0" y="252" width="352" height="178" fill="url(#coverPurple)"/>
    <path d="M352 252 H497 Q512 252 521 270 L523 306 L580 416 H704 V430 H352 Z" fill="url(#coverPurple)"/>
    <path d="M497 252 Q512 252 521 270 L523 306 Z" fill="url(#coverPurple)"/>
    <path d="M521 262 Q530 290 523 306 L515 306 Z" fill="#6b3a9b"/>
    <rect x="523" y="302" width="181" height="4" fill="#e6207a"/>
    <polygon points="523,306 704,306 704,416 580,416" fill="#ffffff"/>
  </svg>

  <div class="brand-name brand-name--back"><span class="dot"></span>Calm Fern Healthcare</div>
  <ul class="contact">
    <li><svg viewBox="0 0 14 14"><rect x=".5" y=".5" width="13" height="13" fill="none" stroke="#fff"/><path d="M7 3a2.6 2.6 0 0 0-2.6 2.6C4.4 8 7 11 7 11s2.6-3 2.6-5.4A2.6 2.6 0 0 0 7 3z" fill="none" stroke="#fff"/></svg>14 Wattle Lane, Harlow WA 6100</li>
    <li><svg viewBox="0 0 14 14"><rect x=".5" y=".5" width="13" height="13" fill="none" stroke="#fff"/><path d="M3 5.5 7 3l4 2.5V11H3z M3 5.5 7 8l4-2.5" fill="none" stroke="#fff"/></svg>admin@calmfernhealthcare.com.au</li>
    <li><svg viewBox="0 0 14 14"><rect x=".5" y=".5" width="13" height="13" fill="none" stroke="#fff"/><path d="M4 3.5 5.6 3 6.5 5 5.5 6a5 5 0 0 0 2.5 2.5l1-1 2 .9-.5 1.6C7 10 4 7 4 3.5z" fill="none" stroke="#fff"/></svg>08 9000 1234</li>
  </ul>

  <h1 class="headline"><span>Reimagining</span><strong>Healthcare</strong></h1>
  <div class="brand-name brand-name--front"><span class="dot"></span>Calm Fern Healthcare</div>

  <svg class="footer-band" width="704" height="36" viewBox="0 0 704 36">
    <polygon points="37,0 666,0 704,36 0,36" fill="#7a42a3"/>
  </svg>
  <div class="footer-url footer-url--left">www.calmfernhealthcare.com.au</div>
  <div class="footer-url footer-url--right">www.calmfernhealthcare.com.au</div>
</section>

<section class="spread spread--inner">
  <div class="services-box">
    <h2 class="section-title">SERVICES</h2>
    <p>Our mission is to supply values driven, responsive, conscientious, and responsible personnel to the aged care sector, disability services, private and public health sectors. Our passion for human services and experience in recruitment, enables us to attract exceptional people with great values ready and willing to make a difference to the lives of vulnerable people.</p>
  </div>

  <div class="personnel">
    <p>We have a comprehensive database<br>of the following personnel</p>
    <ul>
      <li>Registered Nurses (Aged Care, Disability, Emergency, Public and Private healthcare)</li>
      <li>Clinical Nurses</li>
      <li>Nurse Practitioners</li>
      <li>Enrolled Nurses</li>
      <li>Assistants in Nursing (Carers/ PCA’s)</li>
      <li>Support Workers (Disability, Community and Mental health)</li>
      <li>Healthcare Endorsed Chefs and Cooks</li>
      <li>Catering Assistants</li>
      <li>Kitchen hands</li>
      <li>Cleaners</li>
    </ul>
  </div>

  <div class="photo photo--carer-walk" role="img" aria-label="Photo of a nurse walking arm in arm with a laughing elderly woman"></div>

  <div class="about">
    <h2 class="section-title">ABOUT US</h2>
    <p>Calm Fern Healthcare is a staffing provider with a contemporary approach to recruiting and placing exceptional people in human services. We maintain a comprehensive database of General Registered Nurses, Enrolled Nurses, Nursing Assistants, Medication Competent Nursing Assistants, Chefs, Cooks, Catering Assistants, Kitchen hands, Laundry and Cleaning staff. Our staff are skilled in Aged Care, Disability Services, Community Care, Public and Private Healthcare.</p>
    <p style="margin-top:11px">Our vision is to be the most responsive staffing agency in Australia.</p>
  </div>

  <div class="criteria-frame"></div>
  <div class="criteria">
    <div class="photo photo--team" role="img" aria-label="Photo of a smiling group of diverse healthcare staff"></div>
    <h3>ALL STAFF MUST MEET THE FOLLOWING BENCHMARK CRITERIA</h3>
    <ul>
      <li>9 months relevant industry experience in Australia</li>
      <li>National police clearance under 6 months old (must have unsupervised contact for vulnerable groups)</li>
      <li>Qualifications and registrations e.g. Certificate III Individual Support or AHPRA registration</li>
      <li>Excellent communication skills</li>
      <li>A genuine passion for people’s health and wellbeing</li>
      <li>A reliable vehicle and state issued drivers licence</li>
      <li>An understanding of quality and safety outcomes for healthcare providers</li>
      <li>Flexibility and adaptability</li>
    </ul>
  </div>

  <svg class="footer-band" width="704" height="36" viewBox="0 0 704 36">
    <polygon points="37,0 666,0 704,36 0,36" fill="#7a42a3"/>
  </svg>
  <div class="footer-url footer-url--left">www.calmfernhealthcare.com.au</div>
  <div class="footer-url footer-url--right">www.calmfernhealthcare.com.au</div>
</section>

</body>
</html>
```